Psychologist Banner Ads for Remarketing & yarnwave

Brand awareness campaign for tallowbridge.com.au

// Ad Formats //
Static JPEG
Max 45KB in file size
All ads must have a border

// Ad Sizes //
Static: (for Zindle Display network) 300×250, 160×600, 728×90
Static: (for Yarnwave, no more than 25% text): 600×315, 1200 x 627

Please use logo, image and "maximise your wellbeing" from the website home page.

```html
<!DOCTYPE html>
<html lang="en">
<head>
<meta charset="utf-8">
<title>Tallowbridge Psychology – Display Banner Set</title>
<link rel="stylesheet" href="https://fonts.googleapis.com/css2?family=Montserrat:ital,wght@0,400;0,500;0,600;0,700;1,400;1,500&display=swap">
<style>
  :root {
    --stage: #eceeec;
    --ad-border: #ffffff;
    --sky-top: #d6ebf6;
    --sky-bottom: #eef7fb;
    --brand-cyan: #1e9ac4;
    --brand-cyan-dark: #177fa4;
    --brand-navy: #1c4b8d;
    --link-cyan: #1f9bc6;
    --photo-warm: #d9b9a2;
    --curl: #d9dde2;
  }
  * { margin: 0; padding: 0; box-sizing: border-box; }
  html, body { width: 1200px; height: 855px; overflow: hidden; }
  body {
    position: relative;
    background: var(--stage);
    font-family: "Montserrat", Arial, sans-serif;
  }
  .ad {
    position: absolute;
    background: var(--ad-border);
    box-shadow: 0 2px 8px rgba(0,0,0,.18);
    overflow: hidden;
  }
  .ad > * { position: absolute; }

  .photo {
    background: linear-gradient(100deg, var(--sky-top) 0%, var(--sky-bottom) 35%, var(--photo-warm) 60%, var(--sky-bottom) 85%);
  }

  .brand-name {
    color: var(--brand-navy);
    font-weight: 500;
    line-height: 1.1;
    white-space: nowrap;
  }
  .brand-name span { display: block; }

  .tagline {
    color: #fff;
    font-style: italic;
    font-weight: 400;
    letter-spacing: .3px;
  }

  .ribbon { display: block; }
  .ribbon-text {
    color: #fff;
    font-style: italic;
    font-size: 19px;
    white-space: nowrap;
  }

  .cta {
    background: var(--brand-navy);
    color: #fff;
    font-weight: 700;
    font-size: 15px;
    letter-spacing: .3px;
    display: flex;
    align-items: center;
    justify-content: center;
    padding-right: 16px;
    border-radius: 8px 4px 16px 8px;
    white-space: nowrap;
  }
  .cta::after {
    content: "";
    position: absolute;
    right: 0; bottom: 0;
    width: 16px; height: 16px;
    background: linear-gradient(135deg, var(--curl) 0 50%, var(--ad-border) 50%);
    border-top-left-radius: 6px;
  }

  .web-address {
    color: var(--link-cyan);
    font-size: 12.5px;
    white-space: nowrap;
  }

  /* 160 × 600 skyscraper */
  .ad--skyscraper { left: 98px; top: 92px; width: 179px; height: 670px; }
  .ad--skyscraper .sky-panel {
    left: 6px; top: 6px; width: 168px; height: 288px;
    background: linear-gradient(180deg, var(--sky-top), var(--sky-bottom));
  }
  .ad--skyscraper .brand-name { left: 16px; top: 32px; font-size: 20px; }
  .ad--skyscraper .photo { left: 6px; top: 137px; width: 168px; height: 158px;
    background: linear-gradient(180deg, var(--sky-bottom), var(--photo-warm) 70%, var(--sky-bottom)); }
  .ad--skyscraper .tag-band {
    left: 6px; top: 295px; width: 168px; height: 125px;
    background: var(--brand-cyan);
    box-shadow: 0 3px 5px rgba(0,0,0,.2);
    padding: 16px 0 0 12px;
  }
  .ad--skyscraper .tagline { font-size: 23px; line-height: 29px; }
  .ad--skyscraper .cta { left: 15px; top: 565px; width: 150px; height: 38px; }
  .ad--skyscraper .web-address { left: 6px; top: 624px; width: 168px; text-align: center; font-size: 11.5px; }

  /* 300 × 250 medium rectangle */
  .ad--rectangle { left: 303px; top: 246px; width: 335px; height: 279px; }
  .ad--rectangle .photo { left: 6px; top: 6px; width: 324px; height: 201px; }
  .ad--rectangle .ribbon { left: 6px; top: 173px; }
  .ad--rectangle .ribbon-text { left: 19px; top: 178px; }
  .ad--rectangle .cta { left: 25px; top: 215px; width: 149px; height: 38px; }
  .ad--rectangle .web-address { left: 19px; top: 258px; }
  .ad--rectangle .brand-name { left: 214px; top: 218px; font-size: 15px; }

  /* 728 × 90 leaderboard */
  .ad--leaderboard { left: 303px; top: 559px; width: 813px; height: 102px; }
  .ad--leaderboard .photo { left: 6px; top: 6px; width: 467px; height: 90px; }
  .ad--leaderboard .brand-name { left: 16px; top: 18px; font-size: 21px; }
  .ad--leaderboard .ribbon { left: 436px; top: 11px; }
  .ad--leaderboard .ribbon-text { left: 470px; top: 17px; font-size: 20px; }
  .ad--leaderboard .web-address { left: 482px; top: 66px; font-size: 12px; }
  .ad--leaderboard .cta { left: 651px; top: 54px; width: 136px; height: 36px; font-size: 13.5px; }
</style>
</head>
<body>

  <section class="ad ad--skyscraper" aria-label="160 by 600 skyscraper banner">
    <div class="sky-panel"></div>
    <div class="photo" role="img" aria-label="Photo of a smiling woman raising her arms against a pale sky"></div>
    <div class="brand-name"><span>Tallowbridge</span><span>Psychology</span></div>
    <div class="tag-band"><p class="tagline">MAXIMISE<br>YOUR<br>WELLBEING</p></div>
    <a class="cta">LEARN MORE</a>
    <p class="web-address">www.tallowbridge.com.au</p>
  </section>

  <section class="ad ad--rectangle" aria-label="300 by 250 medium rectangle banner">
    <div class="photo" role="img" aria-label="Photo of a smiling woman raising her arms against a pale sky"></div>
    <svg class="ribbon" width="324" height="36" viewBox="0 0 324 36" aria-hidden="true">
      <polygon points="300,4 324,4 316,19 324,34 300,34" fill="var(--brand-cyan-dark)"/>
      <polygon points="0,0 306,0 310,30 0,30" fill="var(--brand-cyan)"/>
    </svg>
    <p class="ribbon-text">MAXIMISE YOUR WELLBEING</p>
    <a class="cta">LEARN MORE</a>
    <p class="web-address">www.tallowbridge.com.au</p>
    <div class="brand-name"><span>Tallowbridge</span><span>Psychology</span></div>
  </section>

  <section class="ad ad--leaderboard" aria-label="728 by 90 leaderboard banner">
    <div class="photo" role="img" aria-label="Photo of a smiling woman raising her arms against a pale sky"></div>
    <div class="brand-name"><span>Tallowbridge</span><span>Psychology</span></div>
    <svg class="ribbon" width="372" height="38" viewBox="0 0 372 38" aria-hidden="true">
      <polygon points="0,4 28,4 28,36 8,36 16,20" fill="var(--brand-cyan-dark)"/>
      <polygon points="22,0 372,0 372,32 26,32" fill="var(--brand-cyan)"/>
    </svg>
    <p class="ribbon-text">MAXIMISE YOUR WELLBEING</p>
    <p class="web-address">www.tallowbridge.com.au</p>
    <a class="cta">LEARN MORE</a>
  </section>

</body>
</html>
```